KORVAN TECH LTD

Advertisement to get more schools:
use website https://www.korvan-tech.co.uk for logos etc.
ICT Service Level Agreements for as little as £2000 per year
Unlimited Remote, phone and email support
Unlimited Call outs included
90% fix time within 30 minutes of ticket submission
Extra support during Quadrel inspections
GDPR service included

```html
<!DOCTYPE html>
<html lang="en">
<head>
<meta charset="utf-8">
<title>KORVAN TECH – Education, Support and Installation</title>
<link rel="stylesheet" href="https://fonts.googleapis.com/css2?family=Roboto:wght@400;500;700&display=swap">
<style>
:root{
  --orange:#f47a3e;
  --orange-ring:#f7b99a;
  --blue:#1e6fb8;
  --navy:#1b3c6e;
  --ink:#222831;
  --card-bg:#ffffff;
  --page-bg:#ffffff;
  --band-bg:#eaf1f8;
  --shadow:rgba(20,40,70,.10);
}
*{margin:0;padding:0;box-sizing:border-box}
html,body{width:1200px;height:3158px;overflow:hidden}
body{font-family:'Roboto',Arial,sans-serif;background:var(--page-bg);color:var(--ink);position:relative}
.site-header{position:absolute;left:0;top:0;width:1200px;height:108px;display:flex;align-items:center;justify-content:space-between;padding:0 75px}
.brand{display:flex;align-items:center;gap:14px}
.brand-mark{width:34px;height:34px;background:var(--blue);border-radius:6px}
.brand-name{font-size:36px;font-weight:700;color:var(--blue);letter-spacing:1px}
.phone-button{background:var(--orange);color:#fff;font-size:28px;font-weight:500;border-radius:8px;padding:14px 20px;letter-spacing:.5px}
.hero{position:absolute;left:0;top:108px;width:1200px;height:673px;background:linear-gradient(180deg,#9fb7cc 0%,#5f86b0 55%,#2e6db0 100%)}
.hero-title{position:absolute;left:0;right:0;bottom:38px;text-align:center;color:#fff;font-size:48px;font-weight:500;line-height:54px}
.features{position:absolute;left:75px;top:903px;width:1050px;display:grid;grid-template-columns:repeat(3,327px);column-gap:34.5px;row-gap:43px}
.feature-card{height:354px;background:var(--card-bg);border-radius:14px;box-shadow:0 3px 18px var(--shadow);display:flex;flex-direction:column;align-items:center;padding-top:42px}
.feature-icon{width:180px;height:180px;border-radius:50%;background:var(--orange-ring);display:flex;align-items:center;justify-content:center}
.feature-icon-inner{width:150px;height:150px;border-radius:50%;background:var(--orange);display:flex;align-items:center;justify-content:center}
.feature-icon svg{width:76px;height:76px;fill:none;stroke:#fff;stroke-width:2.6;stroke-linecap:round;stroke-linejoin:round}
.feature-text{margin-top:26px;text-align:center;font-size:24px;line-height:34px;padding:0 14px}
.partners{position:absolute;left:0;top:1779px;width:1200px;height:246px;background:var(--band-bg);border-top:5px solid var(--orange)}
.partners-heading{text-align:center;margin-top:35px;font-size:26px;color:var(--navy)}
.partners-heading span{display:inline-block;width:26px;height:2px;background:var(--orange);vertical-align:middle;margin-left:8px}
.partner-row{display:flex;justify-content:space-between;align-items:center;padding:0 75px;margin-top:42px}
.partner{display:flex;align-items:center;gap:10px;font-size:36px;font-weight:500;color:var(--navy)}
.partner-box{width:30px;height:30px;background:var(--navy)}
.partner-dot{width:30px;height:30px;border-radius:50%;background:var(--navy)}
.classroom-photo{position:absolute;left:0;top:2025px;width:1200px;height:935px;background:linear-gradient(135deg,#c9c2b8 0%,#9c7a5e 45%,#6d5443 70%,#d9d4cf 100%)}
.site-footer{position:absolute;left:0;top:2978px;width:1200px;text-align:center}
.social-row{display:flex;justify-content:center;gap:16px}
.social-link{width:60px;height:60px;border:2px solid #222;border-radius:50%;display:flex;align-items:center;justify-content:center}
.social-link i{width:10px;height:10px;background:#222;border-radius:50%}
.copyright{margin-top:32px;font-size:24px}
</style>
</head>
<body>
<header class="site-header">
  <div class="brand"><div class="brand-mark"></div><div class="brand-name">KORVAN TECH</div></div>
  <div class="phone-button">0161 555 0142</div>
</header>

<section class="hero" role="img" aria-label="Pupil wearing a virtual reality headset in a school technology lab">
  <h1 class="hero-title">Education, Support and Installation<br>of All Technologies</h1>
</section>

<section class="features">
  <article class="feature-card">
    <div class="feature-icon"><div class="feature-icon-inner">
      <svg viewBox="0 0 64 64"><path d="M16 6h24l8 8v20"/><path d="M16 6v40"/><path d="M40 6v8h8"/><path d="M22 18h16M22 24h20M22 30h14"/><path d="M14 48l10-8 8 6 8-6 10 8-10 8-8-4-8 4z"/></svg>
    </div></div>
    <p class="feature-text">ICT SLA agreements for as little as £2000 per year</p>
  </article>
  <article class="feature-card">
    <div class="feature-icon"><div class="feature-icon-inner">
      <svg viewBox="0 0 64 64"><path d="M8 26l24-18 24 18v28H8z"/><path d="M8 26l24 18 24-18"/><path d="M8 54l18-14M56 54L38 40"/><circle cx="32" cy="24" r="6"/></svg>
    </div></div>
    <p class="feature-text">Unlimited Remote, phone and email support</p>
  </article>
  <article class="feature-card">
    <div class="feature-icon"><div class="feature-icon-inner">
      <svg viewBox="0 0 64 64"><path d="M14 10l10 0 4 12-6 4c3 7 8 12 14 14l4-6 12 4v10c0 2-2 4-4 4C26 52 12 38 10 14c0-2 2-4 4-4z"/><path d="M38 12a14 14 0 0 1 14 14M38 4a22 22 0 0 1 22 22"/></svg>
    </div></div>
    <p class="feature-text">Unlimited Call outs<br>included</p>
  </article>
  <article class="feature-card">
    <div class="feature-icon"><div class="feature-icon-inner">
      <svg viewBox="0 0 64 64"><circle cx="32" cy="32" r="26"/><circle cx="32" cy="32" r="20"/><path d="M32 18v14h10"/></svg>
    </div></div>
    <p class="feature-text">90% fix time within 30 minutes of ticket submission</p>
  </article>
  <article class="feature-card">
    <div class="feature-icon"><div class="feature-icon-inner">
      <svg viewBox="0 0 64 64"><path d="M24 6h26v52H14V16z"/><path d="M42 16h4M42 22h4M42 28h4M42 34h4M42 40h4"/><circle cx="26" cy="30" r="10"/><path d="M33 37l10 10"/></svg>
    </div></div>
    <p class="feature-text">Extra support during Quadrel inspections</p>
  </article>
  <article class="feature-card">
    <div class="feature-icon"><div class="feature-icon-inner">
      <svg viewBox="0 0 64 64"><rect x="8" y="12" width="48" height="34" rx="2"/><path d="M26 54h12M32 46v8"/><rect x="26" y="20" width="12" height="9"/><path d="M28 20v-4a4 4 0 0 1 8 0v4"/><path d="M14 36h36"/></svg>
    </div></div>
    <p class="feature-text">GDPR service<br>included</p>
  </article>
</section>

<section class="partners">
  <h2 class="partners-heading">Partners<span></span></h2>
  <div class="partner-row">
    <div class="partner"><div class="partner-box"></div>Norvel</div>
    <div class="partner">Brightlane</div>
    <div class="partner"><div class="partner-box"></div>Halvex Soft</div>
    <div class="partner"><div class="partner-dot"></div>Tessro</div>
    <div class="partner">Velkar</div>
  </div>
</section>

<section class="classroom-photo" role="img" aria-label="Girl working at a laptop beside a building-block robot in a classroom"></section>

<footer class="site-footer">
  <div class="social-row">
    <a class="social-link"><i></i></a>
    <a class="social-link"><i></i></a>
    <a class="social-link"><i></i></a>
    <a class="social-link"><i></i></a>
  </div>
  <p class="copyright">Copyright © 2022&nbsp; All rights reserved.</p>
</footer>
</body>
</html>
```